Residential improvers, Stillwater Residences *

Quiet Harbor 9 Me is a real estate company specializing in turning unloved properties into improved, happy places to live. We specialize in thoughtfully-improved residential properties for buyers or renters. Our company needs a business card that reflects the renovated homes we create using green and Feng Shui principles,

Please disregard the images we submitted. We are looking for an abstract, sophisticated elegant design. No eggs in a nest ... nothing cute. The image can be soft.
Updates

Aloha (hello) all designers. We are a serious property investment/improvement company. We strive to be unique, renovating with style and elegance. Our business card must portray the same message. We thought the nest and flower might be "it" ... clearly it's not, once we saw what you submitted. Please revisit the brief as it was modified yesterday. Mahalo for your input! We look forward to hearing from all designers that have been invited.

Industry/Entity Type

Real Estate Development

Contact Information for Business Card

We will have separate business cards for
1) Corabeth Danvers 808-555-0173 corabeth@mailtrove.net
2) Trina Vasquell 808-555-0196 trinavasquell@mailtrove.net
** can we add the website later ... in the process of approval.
Investors * Renovators * Connectors

Font styles to use
Sans Serif

Colors
cadf82

Requirements
Must have
• a feng shui feel ... modern. Color - green with black print.
Nice to have
• Stillwater Residences

```html
<!DOCTYPE html>
<html lang="en">
<head>
<meta charset="utf-8">
<title>Stillwater Residences — Business Card</title>
<link href="https://fonts.googleapis.com/css2?family=Quicksand:wght@500;700&display=swap" rel="stylesheet">
<style>
  :root {
    --backdrop: #e6e1da;
    --card-white: #ffffff;
    --brand-green: #cadf82;
    --logo-green: #93b452;
    --leaf-light: #f1f6dc;
    --ink: #111111;
  }
  * { box-sizing: border-box; margin: 0; padding: 0; }
  html, body {
    width: 1200px;
    height: 1200px;
    overflow: hidden;
    background: var(--backdrop);
    font-family: "Quicksand", sans-serif;
    color: var(--ink);
  }
  .canvas { position: relative; width: 1200px; height: 1200px; }
  .card {
    position: absolute;
    left: 276px;
    width: 652px;
    height: 373px;
    border-radius: 12px;
    overflow: hidden;
    box-shadow: 0 4px 10px rgba(0,0,0,0.12);
  }
  .card-front { top: 147px; background: var(--card-white); }
  .card-back { top: 638px; background: var(--brand-green); }

  .brand-name {
    position: absolute;
    left: 60px;
    top: 136px;
    display: flex;
    align-items: center;
    gap: 14px;
    font-weight: 500;
    font-size: 38px;
    line-height: 1;
    color: var(--logo-green);
  }
  .brand-dot {
    width: 16px;
    height: 16px;
    border-radius: 50%;
    background: var(--logo-green);
    flex: none;
  }
  .holder-name {
    position: absolute;
    right: 44px;
    top: 296px;
    font-size: 21px;
    font-weight: 500;
  }
  .holder-name strong { font-weight: 700; }

  .leaf-art {
    position: absolute;
    left: 336px;
    top: 0;
    width: 316px;
    height: 373px;
    background: linear-gradient(160deg, var(--leaf-light) 0%, #e2eebb 60%, var(--brand-green) 100%);
    border-top-left-radius: 70% 40%;
  }
  .contact {
    position: absolute;
    left: 50px;
    top: 280px;
    list-style: none;
    font-size: 21px;
    font-weight: 500;
    line-height: 28px;
  }
  .contact li { display: flex; align-items: center; gap: 8px; }
  .contact svg { width: 17px; height: 17px; fill: var(--ink); }
</style>
</head>
<body>
<main class="canvas">
  <section class="card card-front">
    <div class="brand-name"><span class="brand-dot"></span>Stillwater Residences</div>
    <p class="holder-name">Corabeth <strong>Danvers</strong></p>
  </section>

  <section class="card card-back">
    <div class="leaf-art" role="img" aria-label="White palm frond illustration on green"></div>
    <ul class="contact">
      <li>
        <svg viewBox="0 0 16 16" aria-hidden="true"><path d="M3.5 1l2.5 3-1.5 2c1 2 3 4 5 5l2-1.5 3 2.5-1.5 2.5C7 15 1 9 1 2.5z"/></svg>
        808-555-0173
      </li>
      <li>
        <svg viewBox="0 0 16 16" aria-hidden="true"><path d="M1 3h14v1.2L8 9 1 4.2z"/><path d="M1 5.8l7 4.8 7-4.8V13H1z"/></svg>
        corabeth@mailtrove.net
      </li>
    </ul>
  </section>
</main>
</body>
</html>
```